Birchway Cleaning Commercial Flyer

Would like a flyer that will be used for making sales calls for commercial clients. These flyers will be handed out to Business Owners and facility managers. The flyer must peak interest, introduce the company, and give some information about our services. Birchway Cleaning Services (BWS) is a modern company that is eco-friendly. I have added what the uniform shirt looks like we have one in orange and one in blue. It would be nice to see the pictures you choose have the uniform on.

Target Market(s)

Office Mangers and Facility managers

Industry/Entity Type

Office Cleaning

Font styles to use
Serif

Colors
f78f20
0355a3
abd037

Requirements
Must have
• Modern clean look and feel. The flyer must straight forward and not busy.
• Have sections where bullet points or other written information can be placed
• Must be able to add and move information myself after the design has been decided on.
• Have a section that says:
• To learn more call 301-555-0148 or email info@birchway-tidyco.example
Nice to have
• Some pictures, clean and modern. Peak interest. The uniform to be photoshopped onto the models of the pictures
Should not have
• too busy

```html
<!DOCTYPE html>
<html lang="en">
<head>
<meta charset="utf-8">
<title>Birchway Cleaning Commercial Flyer</title>
<link href="https://fonts.googleapis.com/css2?family=Noto+Serif:ital,wght@0,400;0,600;0,700;1,700&family=Open+Sans:wght@600;700&display=swap" rel="stylesheet">
<style>
  :root{
    --orange:#f78f20;
    --orange-deep:#e9650f;
    --blue:#0355a3;
    --blue-light:#1fb6e6;
    --green:#abd037;
    --green-deep:#3c9a2a;
    --ink:#2d2d2d;
    --text:#333;
    --paper:#ffffff;
    --yellow:#e3f02a;
  }
  *{margin:0;padding:0;box-sizing:border-box}
  html,body{width:848px;height:1200px;overflow:hidden;background:var(--paper)}
  body{font-family:"Noto Serif",serif;color:var(--text)}
  .flyer{position:relative;width:848px;height:1200px;overflow:hidden;
    background:linear-gradient(180deg,#f4f6f8 0%,#eef1f4 45%,#f7f8f9 100%)}
  .backdrop-photo{position:absolute;inset:0 0 260px 0;
    background:linear-gradient(160deg,rgba(255,255,255,.9) 0%,rgba(210,216,222,.55) 55%,rgba(240,242,244,.8) 100%)}
  .hero-photo{position:absolute;right:0;top:20px;width:380px;height:500px;
    background:linear-gradient(180deg,#d9dde1 0%,#c7ccd1 60%,#e3e6e9 100%)}

  .headline{position:absolute;left:52px;top:70px;line-height:1;font-family:"Open Sans",sans-serif;font-weight:700}
  .headline .lead{display:block;font-size:42px;color:var(--ink);font-weight:600;letter-spacing:-.5px}
  .headline .main{display:block;font-size:72px;color:var(--blue);margin-top:10px;letter-spacing:-1px}
  .headline .accent{display:block;font-size:96px;color:var(--orange);margin-top:6px;letter-spacing:-1px}

  .swoosh{position:absolute;left:0;top:380px;width:848px;height:200px}
  .photo-circle{position:absolute;width:210px;height:210px;border-radius:50%;
    border:8px solid var(--green-deep);box-shadow:0 0 0 5px #fff,0 4px 10px rgba(0,0,0,.2)}
  .photo-circle.floor{left:56px;top:378px;background:linear-gradient(160deg,#b9c4cc,#5f6f7b)}
  .photo-circle.window{left:324px;top:378px;background:linear-gradient(160deg,#eef2f4,#c9b8a3)}

  .brand-circle{position:absolute;left:578px;top:486px;width:244px;height:244px;border-radius:50%;
    background:#fff;border:8px solid var(--blue);box-shadow:0 0 0 6px #fff,0 0 0 12px var(--green-deep);
    display:flex;align-items:center;justify-content:center;text-align:center;padding:24px}
  .brand-name{font-size:24px;font-weight:700;color:var(--blue);line-height:1.2}

  .about{position:absolute;left:44px;top:606px;width:520px}
  .about h2{font-size:29px;font-weight:700;color:var(--blue);margin-bottom:8px}
  .about .mission{font-size:16px;font-style:italic;font-weight:700;line-height:1.45}
  .about .detail{font-size:16px;line-height:1.45;margin-top:4px}

  .features{position:absolute;left:210px;top:790px;width:590px;height:205px;
    background:linear-gradient(90deg,var(--orange-deep),var(--orange));border-radius:0 14px 14px 0;
    box-shadow:0 6px 12px rgba(0,0,0,.25);padding:38px 20px 0 78px;list-style:none}
  .features li{font-size:18px;font-weight:700;font-style:italic;color:#fff;margin-bottom:11px;
    display:flex;align-items:center;white-space:nowrap}
  .features li::before{content:"";width:16px;height:11px;border-radius:50% 0;background:var(--green);margin-right:12px;flex:none}

  .leaf-art{position:absolute;right:20px;top:758px;width:110px;height:80px;border-radius:10px;
    background:linear-gradient(135deg,#c8e35a,#4aa12a)}
  .guarantee-seal{position:absolute;left:34px;top:786px;width:200px;height:200px;border-radius:12px;
    background:linear-gradient(180deg,#f3c84a 0%,#e3a11f 60%,#b8262a 100%);box-shadow:0 4px 10px rgba(0,0,0,.25)}

  .social{position:absolute;left:30px;top:1060px}
  .social h3{font-family:"Open Sans",sans-serif;font-size:25px;font-weight:700;color:var(--blue);margin-bottom:14px}
  .social-icons{display:flex;gap:16px}
  .social-icons span{width:46px;height:46px;border-radius:50%;background:#111;display:block}

  .contact-wave{position:absolute;left:0;bottom:0;width:848px;height:250px}
  .contact{position:absolute;right:30px;top:998px;text-align:right;color:#fff;font-style:normal}
  .contact .cta{font-family:"Open Sans",sans-serif;font-size:27px;font-weight:600}
  .contact .phone{font-family:"Open Sans",sans-serif;font-size:36px;font-weight:700;color:var(--yellow);line-height:1.1}
  .contact .place,.contact .web{font-size:18px;font-weight:600;margin-top:3px}
  .learn-more{position:absolute;right:30px;top:1160px;font-size:14px;font-weight:600;color:#fff;text-align:right;white-space:nowrap}
  .learn-more strong{color:var(--yellow);font-weight:700}
</style>
</head>
<body>
<main class="flyer">
  <div class="backdrop-photo" role="img" aria-label="Soft-focus office lobby with a cleaner operating a floor machine"></div>
  <div class="hero-photo" role="img" aria-label="Smiling cleaner in orange cap and uniform pushing a floor scrubber"></div>

  <h1 class="headline">
    <span class="lead">LEAVE THE</span>
    <span class="main">CLEANING</span>
    <span class="accent">TO US!</span>
  </h1>

  <svg class="swoosh" viewBox="0 0 848 200" aria-hidden="true">
    <path d="M0 110 C220 40 520 30 848 120 L848 140 C520 60 240 70 0 140 Z" fill="#abd037"/>
    <path d="M0 140 C240 70 520 60 848 140 L848 152 C520 80 240 90 0 160 Z" fill="#1fb6e6"/>
    <path d="M0 160 C240 90 520 80 848 152 L848 164 C520 96 240 106 0 176 Z" fill="#0355a3"/>
  </svg>

  <div class="photo-circle floor" role="img" aria-label="Cleaner wheeling a janitorial cart across a polished floor"></div>
  <div class="photo-circle window" role="img" aria-label="Cleaner wiping a window frame"></div>

  <div class="brand-circle"><span class="brand-name">Birchway Cleaning Services</span></div>

  <section class="about">
    <h2>ABOUT US</h2>
    <p class="mission">We at Birchway Cleaning Services have one mission – to provide our clients the absolute best service available in the industry.</p>
    <p class="detail">This is done through providing timely, efficient, thoughtful, and thorough service. This is what we call “The Royal Treatment.”</p>
  </section>

  <ul class="features">
    <li>Hospital Grade disinfectants</li>
    <li>Eco-Friendly- microfiber cloths</li>
    <li>HEPA Backpack Vacuums</li>
    <li>Healthy Office/Work Environment is Happy Office</li>
  </ul>
  <div class="leaf-art" role="img" aria-label="Fresh green leaf decoration"></div>
  <div class="guarantee-seal" role="img" aria-label="Gold 100% satisfaction guarantee seal with red ribbon"></div>

  <section class="social">
    <h3>Follow Us at</h3>
    <div class="social-icons"><span></span><span></span><span></span></div>
  </section>

  <svg class="contact-wave" viewBox="0 0 848 250" aria-hidden="true">
    <defs>
      <linearGradient id="waveBlue" x1="0" y1="0" x2="1" y2="0">
        <stop offset="0" stop-color="#1fb6e6"/>
        <stop offset="1" stop-color="#0355a3"/>
      </linearGradient>
    </defs>
    <path d="M120 250 C300 90 560 20 848 40 L848 250 Z" fill="#abd037"/>
    <path d="M170 250 C340 110 580 45 848 60 L848 250 Z" fill="url(#waveBlue)"/>
  </svg>
  <address class="contact">
    <div class="cta">Call Us Now</div>
    <div class="phone">301.555.0148</div>
    <div class="place">Alder Grove, Maryland</div>
    <div class="web">www.birchway-tidyco.example</div>
  </address>
  <p class="learn-more">To learn more call <strong>301-555-0148</strong> or email <strong>info@birchway-tidyco.example</strong></p>
</main>
</body>
</html>
```